Contractor Business Card Design

Looking to have a card made that has a bold description of (KITCHENS, BASEMENTS, BATHROOMS)

Definition and layers a plus

Contact info is;

Mark T. Ellery
Ridgefield, MN 55012
Cell: 612-555-0147
website: www.cobaltfinishworks.example
Email: cobaltfinishworksmn@mailbox.example

colors: red, black, gray, white

Contact Information for Business Card

Contact info is;

Mark T. Ellery
Ridgefield, MN 55012
Cell: 612-555-0147

Colors
ec1f27

Requirements
Must have
• Looking for layers and definition
Nice to have
• Cards are planned to be printed on plastic cards

```html
<!DOCTYPE html>
<html lang="en">
<head>
<meta charset="utf-8">
<title>Cobalt Finish Works – Business Card</title>
<link href="https://fonts.googleapis.com/css2?family=Montserrat:wght@400;600;700&display=swap" rel="stylesheet">
<style>
  :root {
    --backdrop: #141414;
    --card-dark: #232323;
    --card-dark-edge: #1b1b1b;
    --card-light: #f4f4f4;
    --brand-red: #ec1f27;
    --ink: #161616;
    --ink-soft: #555555;
    --emboss: #3a3a3a;
    --emboss-text: #4a4a4a;
  }
  * { margin: 0; padding: 0; box-sizing: border-box; }
  html, body { width: 1200px; height: 869px; overflow: hidden; }
  body {
    background: var(--backdrop);
    font-family: "Montserrat", sans-serif;
    position: relative;
  }

  /* Back of card */
  .card-back {
    position: absolute;
    left: 162px; top: 203px;
    width: 296px; height: 518px;
    background: linear-gradient(160deg, var(--card-dark), var(--card-dark-edge));
    overflow: hidden;
  }
  .card-back .emboss-ring {
    position: absolute;
    left: -40px; top: 0;
    width: 420px; height: 370px;
  }
  .card-back .back-name {
    position: absolute;
    left: 0; right: 0; top: 422px;
    text-align: center;
    color: var(--emboss-text);
    font-weight: 700;
    font-size: 27px;
    line-height: 1.15;
    letter-spacing: 2px;
    text-transform: uppercase;
    white-space: nowrap;
  }

  /* Front of card */
  .card-front {
    position: absolute;
    left: 501px; top: 426px;
    width: 519px; height: 296px;
    background: var(--card-light);
    border-radius: 12px;
    overflow: hidden;
  }
  .card-front .top-band {
    position: absolute;
    left: 0; top: 0; width: 100%; height: 84px;
    background: var(--card-dark);
    border-bottom: 3px solid var(--brand-red);
  }
  .card-front .services {
    position: absolute;
    left: 27px; top: 37px;
    color: var(--brand-red);
    font-weight: 600;
    font-size: 15px;
    white-space: nowrap;
  }
  .card-front .services .divider { color: #bbbbbb; margin: 0 6px; font-weight: 400; }
  .card-front .brand-disc {
    position: absolute;
    left: 356px; top: 23px;
    width: 108px; height: 108px;
    border-radius: 50%;
    background: #ffffff;
    border: 3px solid var(--brand-red);
  }
  .card-front .brand-name {
    position: absolute;
    left: 290px; width: 240px; top: 145px;
    text-align: center;
    color: var(--ink);
    font-weight: 700;
    font-size: 22px;
    line-height: 1.15;
    letter-spacing: 1px;
    text-transform: uppercase;
    white-space: nowrap;
  }
  .card-front .person-name {
    position: absolute;
    left: 27px; top: 158px;
    color: var(--ink);
    font-weight: 700;
    font-size: 21px;
    white-space: nowrap;
  }
  .card-front .contact-list {
    position: absolute;
    left: 27px; top: 197px;
    list-style: none;
  }
  .card-front .contact-list li {
    display: flex; align-items: center;
    height: 17.6px;
    color: var(--ink-soft);
    font-size: 12.5px;
    white-space: nowrap;
  }
  .card-front .contact-list svg {
    width: 11px; height: 11px;
    margin-right: 7px;
    fill: var(--brand-red);
    flex: none;
  }
</style>
</head>
<body>

  <section class="card-back" aria-label="Card back">
    <svg class="emboss-ring" viewBox="0 0 420 370" aria-hidden="true">
      <circle cx="240" cy="185" r="178" fill="none" stroke="var(--emboss)" stroke-width="6"/>
    </svg>
    <p class="back-name">Cobalt<br>Finish Works</p>
  </section>

  <section class="card-front" aria-label="Card front">
    <div class="top-band"></div>
    <p class="services">Kitchens<span class="divider">|</span>Basements<span class="divider">|</span>Bathrooms</p>
    <div class="brand-disc"></div>
    <p class="brand-name">Cobalt<br>Finish Works</p>

    <h1 class="person-name">Mark T. Ellery</h1>
    <ul class="contact-list">
      <li><svg viewBox="0 0 12 12"><path d="M6 0a4 4 0 0 0-4 4c0 3 4 8 4 8s4-5 4-8a4 4 0 0 0-4-4zm0 5.6A1.6 1.6 0 1 1 6 2.4a1.6 1.6 0 0 1 0 3.2z"/></svg>Ridgefield, MN 55012</li>
      <li><svg viewBox="0 0 12 12"><path d="M2.4 0 4.3 2.6 3.2 4a7 7 0 0 0 4.8 4.8L9.4 7.7 12 9.6 10.6 12C5 12 0 7 0 1.4z"/></svg>612-555-0147</li>
      <li><svg viewBox="0 0 12 12"><path d="M0 2h12v1L6 7 0 3zm0 2.3 6 4 6-4V10H0z"/></svg>cobaltfinishworksmn@mailbox.example</li>
      <li><svg viewBox="0 0 12 12"><circle cx="6" cy="6" r="5.3" fill="none" stroke="var(--brand-red)" stroke-width="1.2"/><ellipse cx="6" cy="6" rx="2.2" ry="5.3" fill="none" stroke="var(--brand-red)" stroke-width="1"/><path d="M.7 6h10.6M1.5 3.5h9M1.5 8.5h9" stroke="var(--brand-red)" stroke-width="1"/></svg>www.cobaltfinishworks.example</li>
    </ul>
  </section>

</body>
</html>
```